Business Card Design Project

We require business cards for "Venmoor". We are composed of elite prior military personnel. Our goal is to provide site security for premium businesses who want on the most professional of agents on their premises. Additionally, we will provide executive protection for individuals who require professionalism, flexibility, and dedication

We want this business card to communicate professionalism, dependability, strength. However, we are not an overtly tactical agency and do not want to intimidate our clients personnel or their client. We want to give them a sense of security.
Updates

At the request of one of the designers I've listed the appropriate text that should appear on the card. Please feel free to arrange it in a creative and professional manor.

I've also uploaded a .png file of the triangle logo with no text. Please feel free to incorporate this into your designs.

ThanksĀ 

Target Market(s)

Premium businesses, executives, celebrities, and governments.

Industry/Entity Type

Security

Requirements
Must have
• Text Info that will go on the card. It does not have to be in this order:
Name
Title
Office Phone Number
Cell Phone Number
Email
Website
Mailing Address
Nice to have
• On the back I'd like to see the triangle portion of the logo displayed in a creative way that leaves enough room to write down information if needed.
Should not have
• - Weapons, Globes, or Shields. Every rent-a-cop company has that, and that's not what we are.

```html
<!DOCTYPE html>
<html lang="en">
<head>
<meta charset="utf-8">
<title>Venmoor Business Cards</title>
<link href="https://fonts.googleapis.com/css2?family=PT+Sans:wght@400;700&display=swap" rel="stylesheet">
<style>
  :root {
    --stage: #0e0e0f;
    --card-front: #3b3b3d;
    --card-front-edge: #333335;
    --card-back: #141416;
    --brand-dark: #2a2a2c;
    --brand-light: #cfd0d2;
    --accent: #1e86d4;
    --accent-deep: #1468aa;
    --ink: #151515;
    --paper: #ffffff;
    --paper-shade: #d9d9db;
    --contact: #f2f2f2;
  }
  * { box-sizing: border-box; margin: 0; padding: 0; }
  html, body {
    width: 1200px; height: 871px; overflow: hidden;
    background: var(--stage);
    font-family: "PT Sans", Arial, sans-serif;
  }
  .stage { position: relative; width: 1200px; height: 871px; }

  .card { position: absolute; border-radius: 4px; overflow: hidden;
    box-shadow: 0 18px 40px rgba(0,0,0,.6); }

  /* Back of card */
  .card--back {
    left: 70px; top: 70px; width: 520px; height: 297px;
    background: linear-gradient(125deg, #5a5a5e 0%, #2b2b2e 38%, var(--card-back) 62%, #1b1b1e 100%);
  }
  .card--back .brand {
    position: absolute; left: 92px; top: 96px;
    display: flex; align-items: center; gap: 18px;
  }
  .card--back .brand-mark { width: 40px; height: 40px; background: var(--accent); }
  .card--back .brand-name {
    font-weight: 700; font-size: 64px; letter-spacing: 2px; color: var(--brand-light); line-height: 1;
  }

  /* Front of card */
  .card--front {
    left: 380px; top: 380px; width: 760px; height: 434px;
    background: linear-gradient(160deg, #444447 0%, var(--card-front) 45%, var(--card-front-edge) 100%);
  }
  .card--front .brand {
    position: absolute; left: 70px; top: 52px;
    display: flex; align-items: center; gap: 20px;
  }
  .card--front .brand-mark { width: 44px; height: 44px; background: var(--accent); }
  .card--front .brand-name {
    font-weight: 700; font-size: 74px; letter-spacing: 3px; color: var(--brand-dark); line-height: 1;
  }

  .name-band {
    position: absolute; left: 400px; top: 178px; right: 0; height: 96px;
    border-radius: 16px 0 0 16px;
    background: linear-gradient(90deg, var(--paper) 0%, var(--paper) 55%, var(--paper-shade) 100%);
    padding: 16px 0 0 34px;
  }
  .name-band::after {
    content: ""; position: absolute; right: 0; top: 52px; width: 40px; height: 58px;
    background: var(--accent); border-radius: 10px 0 0 10px;
  }
  .person-name { font-size: 34px; font-weight: 400; color: var(--ink); line-height: 1; letter-spacing: .5px; }
  .person-title { font-size: 18px; color: var(--accent-deep); letter-spacing: .5px; margin-top: 4px; }

  .contact {
    position: absolute; color: var(--contact); font-weight: 700; font-size: 17px; line-height: 26px;
  }
  .contact-row { display: flex; align-items: center; gap: 12px; }
  .contact-key {
    width: 18px; height: 18px; border-radius: 3px; background: var(--accent);
    color: var(--paper); font-size: 11px; line-height: 18px; text-align: center;
  }
  .contact--phones { left: 60px; top: 300px; }
  .contact--web { left: 300px; top: 326px; }
  .contact-address {
    position: absolute; left: 60px; top: 380px; color: var(--contact);
    font-weight: 700; font-size: 17px; letter-spacing: .3px;
  }
</style>
</head>
<body>
<main class="stage">
  <section class="card card--back" aria-label="Card back">
    <div class="brand">
      <span class="brand-mark"></span>
      <span class="brand-name">VENMOOR</span>
    </div>
  </section>

  <section class="card card--front" aria-label="Card front">
    <div class="brand">
      <span class="brand-mark"></span>
      <span class="brand-name">VENMOOR</span>
    </div>

    <div class="name-band">
      <p class="person-name">MARCUS HALE</p>
      <p class="person-title">DIRECTING PARTNER</p>
    </div>

    <div class="contact contact--phones">
      <div class="contact-row"><span class="contact-key">P</span>+1 (555) 318-2046</div>
      <div class="contact-row"><span class="contact-key">F</span>+1 (555) 318-2047</div>
    </div>
    <div class="contact contact--web">
      <div class="contact-row"><span class="contact-key">E</span>MHALE@VENMOOR.COM</div>
      <div class="contact-row"><span class="contact-key">W</span>WWW.VENMOOR.COM</div>
    </div>
    <p class="contact-address">88 HARBOR LANE, EASTFIELD, STATE 40218</p>
  </section>
</main>
</body>
</html>
```